Successful Software Co Launching A Super FUN Mobile & Web Application - ROCKSTAR Designer Needed

Our App is called "Brightly Tally"It is an employee "gamification" app designed to make working at your job fun...Employees complete simple tasks throughout the work day and are rewarded with points they can redeem for different gifts and benefits...We an AMAZING User Interface designed for both the mobile app and website app. We are looking for a clean, modern and simple design... This app is designed to make employees more engaged at work while having fun doing the things they already do each day...They can then redeem their points for rewards. It needs to be easy to understand and simple in its design...Example: A local carpet cleaning business uses our app.Their employees show up to work on time - They get 50 pointsThey clean out their work vehicle - They get 100 pointsThey up-sell an additional cleaning job - The get 250 pointsEtc...The app will also have fun icons and graphics that appear on the screen when an employee accomplishes a task.The app will play fun music sounds when they accomplish tasks too.
Updates

Need extra days to review

Target Market(s)

Small business owners

Logo Text

Brightly Tally

Font styles to use
Sans Serif

Colors

Designer to choose colors to be used in the design.

Requirements
Must have
• Simple elegant design
Nice to have
• I'd like to see examples of fun "icons" that could pop up on the screen after an employee completes a "task" and earns points... Something fun to pop up on the screen... (like a happy face, a thumbs up, fun text bubbles... "Way To Go!" etc... or any other fun ideas)

```html
<!DOCTYPE html>
<html lang="en">
<head>
<meta charset="utf-8">
<title>Brightly Tally – Rewards Home</title>
<link href="https://fonts.googleapis.com/css2?family=Poppins:wght@300;400;500;600&display=swap" rel="stylesheet">
<style>
  :root {
    --page-bg: #eef1f2;
    --screen-bg: #ffffff;
    --ink-soft: #3d3d3d;
    --brand-purple: #c060c0;
    --brand-purple-edge: #5a8fb0;
    --teal: #4fc4c4;
    --teal-dark: #2f9a98;
    --track-grey: #a9b7b6;
    --aqua-card: #5deaea;
    --aqua-edge: #2e9c9a;
    --lime-card: #9eea5e;
    --lime-edge: #4a9a50;
    --lime-text: #8cd24e;
    --white: #ffffff;
  }
  * { box-sizing: border-box; margin: 0; padding: 0; }
  html, body {
    width: 1200px; height: 1032px; overflow: hidden;
    background: var(--page-bg);
    font-family: "Poppins", sans-serif;
  }
  .screen {
    position: absolute; left: 321px; top: 22px;
    width: 558px; height: 988px;
    background: var(--screen-bg);
  }
  .welcome {
    position: absolute; top: 30px; left: 0; width: 100%;
    text-align: center; font-weight: 300; font-size: 29px;
    letter-spacing: 3px; color: var(--ink-soft);
  }
  .welcome-name {
    position: absolute; top: 64px; left: 0; width: 100%;
    text-align: center; font-weight: 600; font-size: 36px;
    color: var(--brand-purple);
  }
  .points-track {
    position: absolute; left: 31px; top: 149px;
    width: 482px; height: 81px; background: var(--track-grey);
  }
  .points-fill {
    position: absolute; left: 0; top: 0; width: 371px; height: 100%;
    background: var(--teal); color: var(--white);
    display: flex; align-items: center; padding-left: 30px; gap: 14px;
  }
  .points-value { font-size: 54px; font-weight: 400; line-height: 1; }
  .points-unit { font-size: 26px; font-weight: 400; padding-top: 8px; }
  .points-goal {
    position: absolute; top: 235px; left: 0; width: 100%;
    display: flex; justify-content: center; align-items: baseline; gap: 14px;
    color: var(--teal-dark);
  }
  .goal-value { font-size: 40px; font-weight: 400; }
  .goal-unit { font-size: 21px; font-weight: 400; }
  .rewards-button {
    position: absolute; left: 43px; top: 319px;
    width: 454px; height: 95px; border-radius: 48px;
    background: var(--brand-purple); border: 2px solid var(--brand-purple-edge);
    color: var(--white); font-size: 32px; font-weight: 400;
    display: flex; align-items: center; justify-content: center;
  }
  .reward-card {
    position: absolute; left: 38px; width: 475px; height: 220px;
    border-radius: 12px; border: 2px solid;
  }
  .reward-card--coffee { top: 452px; background: var(--aqua-card); border-color: var(--aqua-edge); }
  .reward-card--music { top: 707px; background: var(--lime-card); border-color: var(--lime-edge); }
  .cost-pill {
    position: absolute; left: 13px; top: 16px;
    width: 223px; height: 54px; border-radius: 10px;
    background: var(--white); font-size: 28px; font-weight: 600;
    display: flex; align-items: center; justify-content: center;
  }
  .reward-card--coffee .cost-pill { color: var(--teal-dark); }
  .reward-card--music .cost-pill { color: var(--lime-text); }
  .partner-mark {
    position: absolute; right: 30px; top: 40px;
    display: flex; align-items: center; gap: 10px;
    color: var(--white); font-size: 28px; font-weight: 600;
  }
  .partner-dot { width: 22px; height: 22px; border-radius: 50%; background: var(--white); }
  .reward-title {
    position: absolute; right: 36px; bottom: 14px;
    color: var(--white); font-size: 29px; font-weight: 600;
  }
</style>
</head>
<body>
  <main class="screen">
    <p class="welcome">Welcome to</p>
    <h1 class="welcome-name">Brightly Tally, Nora</h1>

    <div class="points-track">
      <div class="points-fill">
        <span class="points-value">2250</span>
        <span class="points-unit">POINTS</span>
      </div>
    </div>

    <p class="points-goal">
      <span class="goal-value">3000</span>
      <span class="goal-unit">POINTS GOAL</span>
    </p>

    <div class="rewards-button">Choose your Rewards</div>

    <section class="reward-card reward-card--coffee">
      <span class="cost-pill">500 POINTS</span>
      <span class="partner-mark"><span class="partner-dot"></span>Beanhouse</span>
      <span class="reward-title">$15 Beanhouse Card</span>
    </section>

    <section class="reward-card reward-card--music">
      <span class="cost-pill">250 POINTS</span>
      <span class="partner-mark"><span class="partner-dot"></span>Tunebox</span>
      <span class="reward-title">$10 Tunebox Card</span>
    </section>
  </main>
</body>
</html>
```